dental sleep medicine stationary
sleep stationary
Project: dental sleep medicine stationary
dental sleep medicine stationary - Health
Creative Brief
Simple
Marcus Holloway, DDS
4153 Brindle Ridge Rd PO Box 362 Corwin Falls, NY 13579
info@pelwardoralcare.example
www.QuietNightBright.example

```html
<!DOCTYPE html>
<html lang="en">
<head>
<meta charset="utf-8">
<title>Stillwater Dental Sleep Care – Business Card</title>
<link href="https://fonts.googleapis.com/css2?family=Cinzel:wght@400;600&family=EB+Garamond:wght@400&display=swap" rel="stylesheet">
<style>
  :root {
    --backdrop: #e6e8ea;
    --blue: #1f6a92;
    --blue-deep: #175579;
    --blue-light: #2b7ba6;
    --tan: #c9a27e;
    --white: #ffffff;
    --ink: #1d5f86;
  }
  html, body {
    margin: 0;
    width: 1200px;
    height: 908px;
    overflow: hidden;
    background: var(--backdrop);
  }
  .canvas {
    position: relative;
    width: 1200px;
    height: 908px;
  }
  .card {
    position: absolute;
    top: 299px;
    width: 540px;
    height: 310px;
    border-radius: 16px;
    overflow: hidden;
    box-shadow: 0 6px 18px rgba(0,0,0,0.18);
  }
  .card-front {
    left: 40px;
    background: linear-gradient(160deg, var(--blue-light) 0%, var(--blue) 55%, var(--blue-deep) 100%);
  }
  .card-back {
    left: 620px;
    background: var(--white);
  }
  .card-art {
    position: absolute;
    inset: 0;
  }
  .front-decor {
    position: absolute;
    left: 150px;
    top: 110px;
    width: 240px;
    height: 180px;
    border-radius: 50%;
    background: radial-gradient(ellipse at center, rgba(255,255,255,0.10) 0%, rgba(255,255,255,0) 70%);
  }
  .brand {
    position: absolute;
    left: 0;
    right: 0;
    margin: 0;
    text-align: center;
    font-family: "Cinzel", serif;
    font-weight: 600;
    font-size: 21px;
    letter-spacing: 0.03em;
    white-space: nowrap;
  }
  .brand-front {
    top: 58px;
    color: var(--white);
  }
  .brand-back {
    top: 66px;
    color: var(--ink);
  }
  .person {
    position: absolute;
    right: 26px;
    top: 148px;
    margin: 0;
    font-family: "Cinzel", serif;
    font-weight: 400;
    font-size: 13px;
    letter-spacing: 0.06em;
    color: var(--ink);
  }
  .contact {
    position: absolute;
    left: 24px;
    top: 206px;
    margin: 0;
    padding: 0;
    list-style: none;
    font-family: "EB Garamond", serif;
    font-size: 11.5px;
    line-height: 1.22;
    color: var(--white);
  }
  .contact li { display: flex; align-items: center; gap: 5px; }
  .contact-icon {
    width: 9px;
    height: 9px;
    flex: none;
  }
</style>
</head>
<body>
<div class="canvas">

  <section class="card card-front" aria-label="Card front">
    <div class="front-decor" role="img" aria-label="Faint decorative sleep motif with small stars"></div>
    <p class="brand brand-front">Stillwater Dental Sleep Care</p>
  </section>

  <section class="card card-back" aria-label="Card back">
    <svg class="card-art" viewBox="0 0 540 310" width="540" height="310" aria-hidden="true">
      <path d="M320,0 C420,8 495,45 540,95 L540,0 Z" fill="var(--blue)"/>
      <path d="M345,0 C430,12 500,48 540,82" fill="none" stroke="var(--white)" stroke-width="3"/>
      <path d="M0,168 C130,150 280,240 540,196" fill="none" stroke="var(--tan)" stroke-width="7"/>
      <path d="M0,182 C130,164 280,254 540,210 L540,310 L0,310 Z" fill="var(--blue)"/>
      <path d="M0,194 C130,176 280,266 540,222" fill="none" stroke="var(--white)" stroke-width="2.5" opacity="0.9"/>
    </svg>

    <p class="brand brand-back">Stillwater Dental Sleep Care</p>

    <p class="person">Marcus Holloway, DDS</p>

    <ul class="contact">
      <li>4153 Brindle Ridge Rd</li>
      <li>PO Box 362</li>
      <li>Corwin Falls, NY 13579</li>
      <li>
        <svg class="contact-icon" viewBox="0 0 10 10" aria-hidden="true"><circle cx="5" cy="5" r="5" fill="var(--white)"/><path d="M3,2.5 L4.2,2.5 L4.6,4 L4,4.5 C4.4,5.4 4.8,5.8 5.6,6.1 L6.1,5.5 L7.5,5.9 L7.5,7.1 C5,7.3 2.8,5 3,2.5 Z" fill="var(--blue)"/></svg>
        555-014-2287
      </li>
      <li>
        <svg class="contact-icon" viewBox="0 0 10 10" aria-hidden="true"><circle cx="5" cy="5" r="5" fill="var(--white)"/><rect x="2.6" y="3.4" width="4.8" height="3.4" fill="var(--blue)"/><rect x="3.4" y="2.4" width="3.2" height="1.4" fill="var(--blue)"/></svg>
        555-014-9063
      </li>
      <li>
        <svg class="contact-icon" viewBox="0 0 10 10" aria-hidden="true"><circle cx="5" cy="5" r="5" fill="var(--white)"/><rect x="2.5" y="3.2" width="5" height="3.6" fill="none" stroke="var(--blue)" stroke-width="0.8"/><path d="M2.5,3.2 L5,5.2 L7.5,3.2" fill="none" stroke="var(--blue)" stroke-width="0.8"/></svg>
        info@pelwardoralcare.example
      </li>
      <li>
        <svg class="contact-icon" viewBox="0 0 10 10" aria-hidden="true"><circle cx="5" cy="5" r="5" fill="var(--white)"/><circle cx="5" cy="5" r="2.6" fill="none" stroke="var(--blue)" stroke-width="0.8"/><path d="M2.4,5 L7.6,5 M5,2.4 L5,7.6" stroke="var(--blue)" stroke-width="0.7"/></svg>
        www.QuietNightBright.example
      </li>
    </ul>
  </section>

</div>
</body>
</html>
```